Bright Harbor Realty

We need a good looking flyer for our real estate company to impress people who are considering to sell their homes for as low as 1.5% listing commission. Please see flyer examples for reference.
555-318-4906

```html
<!DOCTYPE html>
<html lang="en">
<head>
<meta charset="utf-8">
<title>Bright Harbor Realty – 1.5% Listing Commission Flyer</title>
<link href="https://fonts.googleapis.com/css2?family=Lato:wght@400;700;900&display=swap" rel="stylesheet">
<style>
  :root {
    --brand-blue: #2f6fc0;
    --ink: #1d1d1f;
    --slate: #555a60;
    --paper: #f3f3f3;
    --frame: #3a3a3c;
    --sky: #a9c8e6;
    --lawn: #7fa45a;
    --facade: #d9cf9a;
  }
  * { box-sizing: border-box; margin: 0; padding: 0; }
  html, body { width: 1200px; height: 885px; overflow: hidden; }
  body { background: var(--paper); font-family: "Lato", Arial, sans-serif; color: var(--ink); }
  .flyer { position: relative; width: 1200px; height: 885px; background: var(--paper); overflow: hidden; }

  .top-strip { position: absolute; top: 0; left: 0; width: 100%; height: 16px; display: flex; }
  .top-strip .seg-blue { flex: 0 0 62%; background: var(--brand-blue); }
  .top-strip .seg-dark { flex: 1; background: var(--frame); }

  .agent-photo {
    position: absolute; left: 40px; top: 44px; width: 235px; height: 238px;
    border: 4px solid var(--brand-blue); border-radius: 26px;
    background: linear-gradient(160deg, #d8d8d8, #9a9a9a);
  }

  .commission-pill {
    position: absolute; left: 300px; top: 40px; width: 470px; height: 86px;
    background: var(--brand-blue); border-radius: 0 43px 43px 0;
    display: flex; align-items: center; gap: 14px; padding-left: 26px; color: #fff;
  }
  .commission-pill .rate { font-size: 62px; font-weight: 900; letter-spacing: -1px; line-height: 1; }
  .commission-pill .label { font-size: 28px; font-weight: 700; line-height: 1; text-transform: uppercase; }

  .agent-info { position: absolute; left: 300px; top: 136px; }
  .agent-name { font-size: 50px; font-weight: 900; color: var(--slate); letter-spacing: -0.5px; line-height: 1.05; }
  .agent-title { font-size: 24px; font-weight: 700; color: var(--brand-blue); line-height: 1.2; margin-top: 4px; }
  .agent-email { font-size: 20px; color: var(--slate); line-height: 1.2; margin-top: 2px; }
  .agent-phone { font-size: 28px; font-weight: 700; color: var(--slate); line-height: 1.2; margin-top: 2px; letter-spacing: 0.5px; }

  .brand { position: absolute; right: 50px; top: 80px; display: flex; align-items: center; gap: 14px; }
  .brand .mark { width: 46px; height: 46px; background: var(--brand-blue); }
  .brand .name { font-size: 32px; font-weight: 700; color: var(--ink); }

  .exposure-band {
    position: absolute; left: 0; top: 300px; width: 100%; height: 54px;
    background: var(--brand-blue); color: #fff;
    display: flex; align-items: center; justify-content: center;
    font-size: 30px; font-weight: 900; text-transform: uppercase; letter-spacing: 0.5px;
  }

  .pitch { position: absolute; left: 0; top: 380px; width: 100%; text-align: center; }
  .pitch .lead { font-size: 28px; font-weight: 700; line-height: 1.2; }
  .pitch .headline { font-size: 70px; font-weight: 900; color: var(--brand-blue); line-height: 1.1; margin-top: 6px; }
  .pitch .tagline { font-size: 40px; font-weight: 900; color: var(--ink); line-height: 1.2; }

  .home-gallery {
    position: absolute; left: 40px; right: 40px; top: 600px; height: 240px;
    display: flex; gap: 20px;
  }
  .home-photo {
    flex: 1; border: 5px solid var(--frame); border-radius: 26px;
    background: linear-gradient(180deg, var(--sky) 0%, var(--facade) 45%, var(--lawn) 100%);
  }
</style>
</head>
<body>
  <main class="flyer">
    <div class="top-strip"><span class="seg-blue"></span><span class="seg-dark"></span></div>

    <div class="agent-photo" role="img" aria-label="Portrait photo of the real estate broker"></div>

    <div class="commission-pill">
      <span class="rate">1.5%</span>
      <span class="label">Listing<br>Commission</span>
    </div>

    <div class="agent-info">
      <p class="agent-name">YOUR NAME HERE</p>
      <p class="agent-title">Licensed Real Estate Broker</p>
      <p class="agent-email">youremail@brightharbor.com</p>
      <p class="agent-phone">555-318-4906</p>
    </div>

    <div class="brand">
      <span class="mark"></span>
      <span class="name">Bright Harbor Realty</span>
    </div>

    <div class="exposure-band">We do everything to maximize your homes exposure!</div>

    <section class="pitch">
      <p class="lead">We Do Everything to Maximize your Homes Exposure!</p>
      <p class="headline">List For 1.5% Commission</p>
      <p class="tagline">Still Receive Top Market</p>
    </section>

    <section class="home-gallery">
      <div class="home-photo" role="img" aria-label="Photo of a yellow single-story home with garage and trees"></div>
      <div class="home-photo" role="img" aria-label="Photo of a two-story home with driveway and palm trees"></div>
      <div class="home-photo" role="img" aria-label="Photo of a home with garage, lawn and tropical plants"></div>
      <div class="home-photo" role="img" aria-label="Photo of a two-story home seen from the street"></div>
    </section>
  </main>
</body>
</html>
```